Modern Logo for Law Firm
TORVE LAW FIRM
Project: Modern Logo for Law Firm
Modern Logo for Law Firm - Law
Creative Brief
Professional
Lucian Pertovalli, Esq.
Attorney at Law
3817 Carmody Ave., Suite 200 Beverly Hills, CA 90212
lp@torvelawfirm.example
www.torvelawfirm.example
We are open to all types of creative fonts...
We would prefer to have only our logo on the back with maybe our web address

```html
<!DOCTYPE html>
<html lang="en">
<head>
<meta charset="utf-8">
<title>Torve Law Firm – Stationery</title>
<link href="https://fonts.googleapis.com/css2?family=Playfair+Display:wght@700&family=Open+Sans:wght@400;600&display=swap" rel="stylesheet">
<style>
:root{
  --stage:#3b3b3b;
  --paper:#ffffff;
  --navy:#1f3a7a;
  --blue:#2d6fc4;
  --gold:#f0a41e;
  --ink:#333;
  --muted:#9a9a9a;
}
*{box-sizing:border-box;margin:0;padding:0}
html,body{width:1200px;height:238px;overflow:hidden;background:var(--stage);font-family:"Open Sans",sans-serif;color:var(--ink)}
.canvas{position:relative;width:1200px;height:238px}
.piece{position:absolute;background:var(--paper);overflow:hidden}
.wordmark{display:flex;align-items:center;gap:4px;font-family:"Playfair Display",serif;font-weight:700;color:var(--navy);white-space:nowrap;line-height:1}
.wordmark .dot{border-radius:50%;background:var(--gold);flex:none}
.wordmark.light{color:#fff}
.band{position:absolute;left:0;width:100%}
.tiny{font-size:3px;line-height:1.4;color:var(--ink)}
.line{height:1.5px;background:#d6d6d6;margin-bottom:2px}
.navy-bg{background:var(--navy)}
.gold-bg{background:var(--gold)}
.screen-dark{background:#0b0b0b}
.title{font-size:4px;font-weight:600;color:var(--navy)}
</style>
</head>
<body>
<div class="canvas">

  <!-- logo panel -->
  <div class="piece" style="left:6px;top:6px;width:138px;height:78px;display:flex;align-items:center;justify-content:center">
    <div class="wordmark" style="font-size:14px"><span class="dot" style="width:12px;height:12px"></span>TORVE LAW FIRM</div>
  </div>

  <!-- business cards -->
  <div class="piece" style="left:6px;top:92px;width:66px;height:38px;display:flex;align-items:center;justify-content:center">
    <div class="wordmark" style="font-size:6px"><span class="dot" style="width:5px;height:5px"></span>TORVE LAW FIRM</div>
  </div>
  <div class="piece navy-bg" style="left:78px;top:92px;width:66px;height:38px;display:flex;align-items:center;justify-content:center">
    <div class="wordmark light" style="font-size:6px"><span class="dot" style="width:5px;height:5px"></span>TORVE LAW FIRM</div>
  </div>
  <div class="piece" style="left:6px;top:136px;width:66px;height:38px;padding:4px">
    <div class="wordmark" style="font-size:4px"><span class="dot" style="width:3px;height:3px"></span>TORVE LAW FIRM</div>
    <div class="title" style="margin-top:4px">Lucian Pertovalli, Esq.</div>
    <div class="tiny">Attorney at Law<br>3817 Carmody Ave., Suite 200<br>lp@torvelawfirm.example</div>
    <svg class="band" style="bottom:0;height:6px" viewBox="0 0 66 6" preserveAspectRatio="none"><path d="M0 6 Q33 0 66 3 V6Z" fill="var(--blue)"/><path d="M0 6 Q33 3 66 5 V6Z" fill="var(--gold)"/></svg>
  </div>
  <div class="piece" style="left:78px;top:136px;width:66px;height:38px;display:flex;align-items:center;justify-content:center">
    <div class="tiny" style="font-size:4px;color:var(--navy)">www.torvelawfirm.example</div>
    <svg class="band" style="bottom:0;height:6px" viewBox="0 0 66 6" preserveAspectRatio="none"><path d="M0 6 Q33 0 66 3 V6Z" fill="var(--navy)"/><path d="M0 6 Q33 3 66 5 V6Z" fill="var(--gold)"/></svg>
  </div>

  <!-- letterheads -->
  <div class="piece" style="left:162px;top:28px;width:72px;height:184px;padding:8px 7px">
    <div class="wordmark" style="font-size:5px"><span class="dot" style="width:4px;height:4px"></span>TORVE LAW FIRM</div>
    <div class="tiny" style="margin:12px 0 4px">Dear Client,</div>
    <div class="line"></div><div class="line"></div><div class="line" style="width:70%"></div>
    <div class="tiny" style="position:absolute;bottom:14px;left:7px">www.torvelawfirm.example</div>
    <svg class="band" style="bottom:0;height:12px" viewBox="0 0 72 12" preserveAspectRatio="none"><path d="M0 12 Q36 0 72 6 V12Z" fill="var(--navy)"/><path d="M0 12 Q36 5 72 9 V12Z" fill="var(--gold)"/></svg>
  </div>
  <div class="piece" style="left:240px;top:28px;width:72px;height:184px;padding:8px 7px">
    <div class="wordmark" style="font-size:5px"><span class="dot" style="width:4px;height:4px"></span>TORVE LAW FIRM</div>
    <div class="tiny" style="margin:12px 0 4px">Dear Client,</div>
    <div class="line"></div><div class="line"></div><div class="line"></div><div class="line" style="width:60%"></div>
    <div class="tiny" style="position:absolute;bottom:14px;left:7px">lp@torvelawfirm.example</div>
    <svg class="band" style="bottom:0;height:12px" viewBox="0 0 72 12" preserveAspectRatio="none"><path d="M0 12 Q36 0 72 6 V12Z" fill="var(--blue)"/><path d="M0 12 Q36 5 72 9 V12Z" fill="var(--gold)"/></svg>
  </div>

  <!-- compliment slips -->
  <div class="piece" style="left:330px;top:28px;width:78px;height:52px;padding:5px">
    <div class="wordmark" style="font-size:4px"><span class="dot" style="width:3px;height:3px"></span>TORVE LAW FIRM</div>
    <div class="title" style="margin-top:8px">With Compliments</div>
    <svg class="band" style="bottom:0;height:7px" viewBox="0 0 78 7" preserveAspectRatio="none"><path d="M0 7 Q39 0 78 3 V7Z" fill="var(--navy)"/><path d="M0 7 Q39 3 78 5 V7Z" fill="var(--gold)"/></svg>
  </div>
  <div class="piece" style="left:330px;top:90px;width:78px;height:52px;padding:5px">
    <div class="wordmark" style="font-size:4px"><span class="dot" style="width:3px;height:3px"></span>TORVE LAW FIRM</div>
    <div class="title" style="margin-top:8px">With Compliments</div>
    <svg class="band" style="bottom:0;height:7px" viewBox="0 0 78 7" preserveAspectRatio="none"><path d="M0 7 Q39 0 78 3 V7Z" fill="var(--blue)"/><path d="M0 7 Q39 3 78 5 V7Z" fill="var(--gold)"/></svg>
  </div>

  <!-- envelopes -->
  <div class="piece" style="left:424px;top:28px;width:110px;height:52px;padding:5px">
    <div class="wordmark" style="font-size:4px"><span class="dot" style="width:3px;height:3px"></span>TORVE LAW FIRM</div>
    <svg class="band" style="bottom:0;height:8px" viewBox="0 0 110 8" preserveAspectRatio="none"><path d="M0 8 Q55 0 110 4 V8Z" fill="var(--navy)"/><path d="M0 8 Q55 4 110 6 V8Z" fill="var(--gold)"/></svg>
  </div>
  <div class="piece" style="left:424px;top:90px;width:110px;height:52px;padding:5px">
    <div class="wordmark" style="font-size:4px"><span class="dot" style="width:3px;height:3px"></span>TORVE LAW FIRM</div>
    <svg class="band" style="bottom:0;height:8px" viewBox="0 0 110 8" preserveAspectRatio="none"><path d="M0 8 Q55 0 110 4 V8Z" fill="var(--blue)"/><path d="M0 8 Q55 4 110 6 V8Z" fill="var(--gold)"/></svg>
  </div>
  <div class="piece navy-bg" style="left:550px;top:90px;width:84px;height:52px">
    <svg style="position:absolute;inset:0" viewBox="0 0 84 52"><path d="M0 0 L42 26 L84 0Z" fill="#fff"/></svg>
  </div>
  <div class="piece gold-bg" style="left:640px;top:90px;width:84px;height:52px">
    <svg style="position:absolute;inset:0" viewBox="0 0 84 52"><path d="M0 0 L42 26 L84 0Z" fill="var(--navy)"/></svg>
  </div>

  <!-- tablet screen -->
  <div class="piece screen-dark" style="left:890px;top:22px;width:112px;height:170px;display:flex;align-items:center;justify-content:center">
    <div class="wordmark light" style="font-size:9px"><span class="dot" style="width:8px;height:8px"></span>TORVE LAW FIRM</div>
  </div>

  <!-- phone screens -->
  <div class="piece" style="left:1030px;top:44px;width:58px;height:104px;display:flex;align-items:center;justify-content:center">
    <div class="wordmark" style="font-size:4.5px"><span class="dot" style="width:4px;height:4px"></span>TORVE LAW FIRM</div>
  </div>
  <div class="piece" style="left:1126px;top:44px;width:58px;height:104px;display:flex;align-items:center;justify-content:center">
    <div class="wordmark" style="font-size:4.5px"><span class="dot" style="width:4px;height:4px"></span>TORVE LAW FIRM</div>
  </div>

</div>
</body>
</html>
```